to-go container produts catalogue

we sell different kinds of to-go containers and need to make a catalogue for our cosumers.
Most of them are restraunts owner and some of them are distrunutors.
Our company named "Copper Lantern Packaging"
Our website is www.copperlanternpackaging.example
our produts are quite like we showed on web.
We also have other produtcs need to be showed in the catalogue
We have different product lines and each type have different size.
We hope the catalogue is simple and clear. maybe a little industrial style

```html
<!DOCTYPE html>
<html lang="en">
<head>
<meta charset="utf-8">
<title>Copper Lantern Packaging – Catalogue</title>
<link href="https://fonts.googleapis.com/css2?family=Montserrat:wght@400;500;600;700;800&display=swap" rel="stylesheet">
<style>
  :root{
    --bg:#e6e7e8;
    --paper:#ffffff;
    --mint:#cdeedb;
    --mint-soft:#e3f6eb;
    --green:#86cfa3;
    --green-deep:#4f9e72;
    --ink:#333a36;
    --ink-soft:#55605a;
    --photo-a:#8fd9b5;
    --photo-b:#5fbf92;
    --photo-c:#b9e6cd;
    --black-pack:#2b2d2e;
    --white-pack:#eef0ef;
  }
  *{box-sizing:border-box;margin:0;padding:0}
  html,body{width:1200px;height:1034px;overflow:hidden}
  body{background:var(--bg);font-family:"Montserrat",sans-serif;color:var(--ink);position:relative}

  .spread{position:absolute;left:50px;width:1100px;display:flex;background:var(--paper);box-shadow:0 4px 18px rgba(0,0,0,.12)}
  .spread--outside{top:26px;height:440px}
  .spread--inside{top:494px;height:514px}
  .page{width:550px;height:100%;position:relative;overflow:hidden}
  .page + .page{border-left:1px solid #e2e2e2}

  /* outside */
  .cover-art{position:absolute;inset:14px;border-radius:14px;
    background:radial-gradient(circle at 30% 25%,var(--photo-c),transparent 45%),
               radial-gradient(circle at 75% 70%,var(--photo-c),transparent 40%),
               linear-gradient(135deg,var(--photo-a),var(--photo-b))}
  .about-box{position:absolute;left:140px;top:92px;width:270px;height:240px;background:var(--paper);
    display:flex;flex-direction:column;align-items:center;justify-content:center;text-align:center;gap:9px;padding:14px 18px}
  .about-box p{font-size:8.4px;line-height:1.45;color:var(--ink)}
  .contact-item{display:flex;flex-direction:column;align-items:center;gap:2px;font-size:8.4px}
  .contact-item svg{width:9px;height:9px;fill:var(--ink)}
  .brand-plate{position:absolute;left:250px;bottom:66px;width:230px;height:90px;background:var(--paper);
    display:flex;align-items:center;justify-content:center;gap:10px;padding:10px}
  .brand-plate .mark{width:16px;height:16px;background:var(--green-deep);flex:none}
  .brand-plate span{font-size:18px;font-weight:800;color:var(--green-deep);line-height:1.1;text-transform:uppercase}

  /* inside */
  .section-band{position:absolute;top:14px;height:34px;display:flex;align-items:center;
    font-weight:800;font-size:15px;color:#fff;letter-spacing:.3px}
  .section-band--left{left:14px;width:520px;padding-left:34px;
    background:linear-gradient(100deg,var(--green-deep) 0 8%,var(--green) 8% 72%,var(--mint) 72%);border-radius:10px 0 0 10px}
  .section-band--right{right:14px;width:520px;justify-content:flex-end;padding-right:90px;
    background:linear-gradient(100deg,var(--mint) 0 28%,var(--green) 28% 88%,var(--green-deep) 88%);border-radius:0 10px 10px 0}
  .card-grid{position:absolute;top:58px;left:14px;right:14px;bottom:14px;display:grid;
    grid-template-columns:1fr 1fr;grid-template-rows:1fr 1fr;gap:12px}
  .product-card{border:2px solid var(--green);border-radius:10px;overflow:hidden;display:flex;flex-direction:column;background:var(--paper)}
  .product-title{background:var(--mint);text-align:center;font-size:10.5px;font-weight:500;line-height:1.2;padding:6px 8px;min-height:36px;
    display:flex;align-items:center;justify-content:center}
  .product-photo{flex:1;display:flex;align-items:center;justify-content:center}
  .product-photo .shape{width:110px;height:54px;border-radius:12px}
  .shape--black{background:linear-gradient(160deg,#55595a,var(--black-pack) 60%)}
  .shape--white{background:linear-gradient(160deg,#fff,var(--white-pack));border:1px solid #d6dad8}
  .product-info{background:var(--mint-soft);display:flex;justify-content:space-between;padding:6px 8px;gap:6px;
    border-top:1px solid var(--mint)}
  .specs{list-style:none;font-size:7.6px;line-height:1.32;color:var(--ink-soft)}
  .badges{display:grid;grid-template-columns:repeat(2,44px);gap:4px 2px;align-content:center}
  .badge{display:flex;flex-direction:column;align-items:center;font-size:5.6px;font-weight:800;text-align:center;line-height:1.05;color:var(--ink)}
  .badge svg{width:15px;height:15px;stroke:var(--ink);fill:none;stroke-width:1.6;margin-bottom:2px}
</style>
</head>
<body>

<svg width="0" height="0" style="position:absolute" aria-hidden="true">
  <symbol id="icon-leak" viewBox="0 0 20 20"><circle cx="10" cy="10" r="8"/><path d="M10 5c-2 3-3 4.5-3 6a3 3 0 0 0 6 0c0-1.5-1-3-3-6z"/><path d="M4 16L16 4"/></symbol>
  <symbol id="icon-recycle" viewBox="0 0 20 20"><path d="M10 3l3.5 6M16 12l-2 4H6M4 12l3-6"/><path d="M11.5 3.5L10 3l-.5 1.8M15 15.5l1-3.5-1.8-.6M5 5.5l2 .5.3-1.8"/></symbol>
  <symbol id="icon-bpa" viewBox="0 0 20 20"><circle cx="10" cy="10" r="8"/><circle cx="10" cy="10" r="4.5"/></symbol>
  <symbol id="icon-micro" viewBox="0 0 20 20"><rect x="2" y="4" width="16" height="12" rx="1.5"/><rect x="4.5" y="6.5" width="8" height="7"/><path d="M15 7v1M15 10v1"/></symbol>
</svg>

<!-- OUTSIDE SPREAD -->
<section class="spread spread--outside">
  <div class="page page--back">
    <div class="cover-art" role="img" aria-label="Photo of green and kraft take-out containers, cups and cutlery behind a white triangular lattice"></div>
    <div class="about-box">
      <p>We at Copper Lantern Packaging are committed to providing high quality disposable goods to our customers. We are a small business based in Brookvale, California. We specialize in customization of cutlery, napkins, and other disposables.</p>
      <p>Contact us 24/7 our team of sales is ready to serve.</p>
      <div class="contact-item">
        <svg viewBox="0 0 10 10"><path d="M5 0a3.5 3.5 0 0 0-3.5 3.5C1.5 6 5 10 5 10s3.5-4 3.5-6.5A3.5 3.5 0 0 0 5 0zm0 5a1.4 1.4 0 1 1 0-2.8A1.4 1.4 0 0 1 5 5z"/></svg>
        <span>1180 Foundry Ave.<br>Brookvale, CA 90210</span>
      </div>
      <div class="contact-item">
        <svg viewBox="0 0 10 10"><path d="M2 0l2 2.3-1 1.3a6 6 0 0 0 3.4 3.4l1.3-1L10 8l-1.3 1.6C4.5 10 0 5.5.4 1.3z"/></svg>
        <span>555-014-2288</span>
      </div>
      <div class="contact-item">
        <svg viewBox="0 0 10 10"><path d="M0 2h10v6H0z M0 2l5 3.5L10 2" fill="none" stroke="#333a36"/></svg>
        <span>cs@copperlanternpackaging.example</span>
      </div>
    </div>
  </div>
  <div class="page page--front">
    <div class="cover-art" role="img" aria-label="Photo of green disposable food containers, lids and cups behind a white triangular lattice"></div>
    <div class="brand-plate"><i class="mark"></i><span>Copper Lantern Packaging</span></div>
  </div>
</section>

<!-- INSIDE SPREAD -->
<section class="spread spread--inside">
  <div class="page page--microwave">
    <h2 class="section-band section-band--left">Microwaveable Take-Out Containers</h2>
    <div class="card-grid">
      <article class="product-card">
        <h3 class="product-title">58oz Microwaveable Container with Lid, 150 sets</h3>
        <div class="product-photo"><div class="shape shape--black" role="img" aria-label="Black rectangular container with clear lid"></div></div>
        <div class="product-info">
          <ul class="specs"><li>Color:Black/White Base, Clear Lid</li><li>Capacity:58 oz</li><li>Material:PP</li><li>Product Weight:84g ± 1g</li><li>Case Pack:150</li><li>Case Weight:28.68 lb</li><li>Case Dimension:62.5*29*34.5 cm</li></ul>
          <div class="badges">
            <span class="badge"><svg><use href="#icon-leak"/></svg>LEAK PROOF</span><span class="badge"><svg><use href="#icon-recycle"/></svg>RECYCLABLE</span>
            <span class="badge"><svg><use href="#icon-bpa"/></svg>BPA FREE</span><span class="badge"><svg><use href="#icon-micro"/></svg>MICROWAVE SAFE</span>
          </div>
        </div>
      </article>
      <article class="product-card">
        <h3 class="product-title">48oz Square Microwaveable Container with Lid 3-compartment, 100 sets</h3>
        <div class="product-photo"><div class="shape shape--black" style="width:76px;height:66px" role="img" aria-label="Black square three-compartment container"></div></div>
        <div class="product-info">
          <ul class="specs"><li>Color:Black/White Base, Clear Lid</li><li>Capacity:48 oz</li><li>Material:PP</li><li>Product Weight:84g ± 1g</li><li>Case Pack:100</li><li>Case Weight:19.4 lb</li><li>Case Dimension:42.5*21.8*43.7 cm</li></ul>
          <div class="badges">
            <span class="badge"><svg><use href="#icon-leak"/></svg>LEAK PROOF</span><span class="badge"><svg><use href="#icon-recycle"/></svg>RECYCLABLE</span>
            <span class="badge"><svg><use href="#icon-bpa"/></svg>BPA FREE</span><span class="badge"><svg><use href="#icon-micro"/></svg>MICROWAVE SAFE</span>
          </div>
        </div>
      </article>
      <article class="product-card">
        <h3 class="product-title">39oz Rectangular Microwaveable Container with Lid 3-compartment, 150 sets</h3>
        <div class="product-photo"><div class="shape shape--black" role="img" aria-label="Black rectangular three-compartment container"></div></div>
        <div class="product-info">
          <ul class="specs"><li>Color:Black/White Base, Clear Lid</li><li>Capacity:39 oz</li><li>Material:PP</li><li>Product Weight:72g ± 1g</li><li>Case Pack:150</li><li>Case Weight:25.88 lb</li><li>Case Dimension:59*25.5*39 cm</li></ul>
          <div class="badges">
            <span class="badge"><svg><use href="#icon-leak"/></svg>LEAK PROOF</span><span class="badge"><svg><use href="#icon-recycle"/></svg>RECYCLABLE</span>
            <span class="badge"><svg><use href="#icon-bpa"/></svg>BPA FREE</span><span class="badge"><svg><use href="#icon-micro"/></svg>MICROWAVE SAFE</span>
          </div>
        </div>
      </article>
      <article class="product-card">
        <h3 class="product-title">38oz Rectangular Microwaveable Container with Lid, 150 sets</h3>
        <div class="product-photo"><div class="shape shape--black" role="img" aria-label="Black rectangular container with clear lid"></div></div>
        <div class="product-info">
          <ul class="specs"><li>Color:Black/White Base, Clear Lid</li><li>Capacity:38 oz</li><li>Material:PP</li><li>Product Weight:54g ± 1g</li><li>Case Pack:150</li><li>Case Weight:17.35 lb</li><li>Case Dimension:48*23.7*48 cm</li></ul>
          <div class="badges">
            <span class="badge"><svg><use href="#icon-leak"/></svg>LEAK PROOF</span><span class="badge"><svg><use href="#icon-recycle"/></svg>RECYCLABLE</span>
            <span class="badge"><svg><use href="#icon-bpa"/></svg>BPA FREE</span><span class="badge"><svg><use href="#icon-micro"/></svg>MICROWAVE SAFE</span>
          </div>
        </div>
      </article>
    </div>
  </div>

  <div class="page page--clamshell">
    <h2 class="section-band section-band--right">Clamshell Contaier</h2>
    <div class="card-grid">
      <article class="product-card">
        <h3 class="product-title">Clamshell Container 3-Compartment, Center Slide, 9.5"x 9.25"</h3>
        <div class="product-photo"><div class="shape shape--white" style="width:80px;height:66px" role="img" aria-label="White three-compartment clamshell container"></div></div>
        <div class="product-info">
          <ul class="specs"><li>Color: White</li><li>Capacity:36 oz</li><li>Material:MFPP</li><li>Case Pack:150 Sets</li><li>Case Weight:22.05 lb</li><li>Case Dimension:</li><li>20.08"x11.02"x10.04"</li></ul>
          <div class="badges">
            <span class="badge"><svg><use href="#icon-leak"/></svg>LEAK PROOF</span><span class="badge"><svg><use href="#icon-recycle"/></svg>RECYCLABLE</span>
            <span class="badge"><svg><use href="#icon-bpa"/></svg>BPA FREE</span><span class="badge"><svg><use href="#icon-micro"/></svg>MICROWAVE SAFE</span>
          </div>
        </div>
      </article>
      <article class="product-card">
        <h3 class="product-title">Clamshell Container, Center Slide, 9.5"x9.25"</h3>
        <div class="product-photo"><div class="shape shape--white" style="width:80px;height:66px" role="img" aria-label="White single-compartment clamshell container"></div></div>
        <div class="product-info">
          <ul class="specs"><li>Color: White</li><li>Capacity:40 oz</li><li>Material:MFPP</li><li>Case Pack:150 Sets</li><li>Case Weight:22.05 lb</li><li>Case Dimension:</li><li>20.47"x11.02"x10.04"</li></ul>
          <div class="badges">
            <span class="badge"><svg><use href="#icon-leak"/></svg>LEAK PROOF</span><span class="badge"><svg><use href="#icon-recycle"/></svg>RECYCLABLE</span>
            <span class="badge"><svg><use href="#icon-bpa"/></svg>BPA FREE</span><span class="badge"><svg><use href="#icon-micro"/></svg>MICROWAVE SAFE</span>
          </div>
        </div>
      </article>
      <article class="product-card">
        <h3 class="product-title">Clamshell Container 3-Compartment, Corner Lock, 9"x 9"</h3>
        <div class="product-photo"><div class="shape shape--white" style="width:96px;height:62px" role="img" aria-label="Open white three-compartment clamshell with corner lock"></div></div>
        <div class="product-info">
          <ul class="specs"><li>Color: White</li><li>Capacity:25 oz</li><li>Material:MFPP</li><li>Case Pack:150 Sets</li><li>Case Weight:22 lb</li><li>Case Dimension:</li><li>17.72"x17.72"x9.45</li></ul>
          <div class="badges">
            <span class="badge"><svg><use href="#icon-leak"/></svg>LEAK PROOF</span><span class="badge"><svg><use href="#icon-recycle"/></svg>RECYCLABLE</span>
            <span class="badge"><svg><use href="#icon-bpa"/></svg>BPA FREE</span><span class="badge"><svg><use href="#icon-micro"/></svg>MICROWAVE SAFE</span>
          </div>
        </div>
      </article>
      <article class="product-card">
        <h3 class="product-title">Clamshell Container, Center Slide, 8.8"x5.3"</h3>
        <div class="product-photo"><div class="shape shape--white" role="img" aria-label="White rectangular clamshell container"></div></div>
        <div class="product-info">
          <ul class="specs"><li>Color: White</li><li>Capacity:24 oz</li><li>Material:MFPP</li><li>Case Pack:200 Sets</li><li>Case Weight:19.18 lb</li><li>Case Dimension:</li><li>15.75"x12.40"x9.45"</li></ul>
          <div class="badges">
            <span class="badge"><svg><use href="#icon-leak"/></svg>LEAK PROOF</span><span class="badge"><svg><use href="#icon-recycle"/></svg>RECYCLABLE</span>
            <span class="badge"><svg><use href="#icon-bpa"/></svg>BPA FREE</span><span class="badge"><svg><use href="#icon-micro"/></svg>MICROWAVE SAFE</span>
          </div>
        </div>
      </article>
    </div>
  </div>
</section>

</body>
</html>
```